Fernvale Pte Ltd

I want a creative and stand out web page so when my client search for my web page or google search. The front page is stand out and they know that we are the interior office designer that are searching for . We are commercial office design company. We also have the video to put at our front page for client to see. Natural is the key elements. As we like to carry recycle materials , plant , trees is our key element such as biophilic design
Updates

Hi All,

For my web page, I need minimalist design and creative frontpage.
When my client search for my web page, they straight feel that this is the office design company.
The webpage is special and nature is the key element for the design.
My company logo can be design in the shaped of the letter OO in the webpage.
Below is the sample you can refer.

https://www.pinboardly.example/pin/592716408361528037/

Target Market(s)

Customer searching for office design

Industry/Entity Type

Commerical designer firm- Office interior design & Build company

Number of Pages Required

5+ page

Font styles to use
Other font styles liked:
• Wilmina

Colors
59FF00
82FF00
B8FF75
E3FFCB
F4FFEA
FFC000
F8CF3A
FAE287
FDF2CF
FEFAEE
6B429C
8869AF
B7A5CE
E3DAEB
F3F0F8

Requirements
Must have
• Home, Services,Gallery, Calculator, Testimonials, Contact, Blog
Nice to have
• Natural, creative, minimalist
Should not have
• No black color or blue color

```html
<!DOCTYPE html>
<html lang="en">
<head>
<meta charset="utf-8">
<title>Fernvale Pte Ltd — Office Interior Design &amp; Renovation</title>
<link href="https://fonts.googleapis.com/css2?family=Questrial&display=swap" rel="stylesheet">
<style>
:root{
  --deep:#04202b;
  --lime:#82ff00;
  --amber:#ffc000;
  --violet:#6b429c;
  --cream:#fefaee;
  --ink:#2a2a2a;
  --white:#ffffff;
}
*{margin:0;padding:0;box-sizing:border-box}
html,body{width:1200px;height:2848px;overflow:hidden}
body{font-family:"Questrial",sans-serif;background:var(--deep);color:var(--white);position:relative}
.abs{position:absolute}
a{color:inherit;text-decoration:none}

.hero-art{left:0;top:0;width:1200px;height:770px;
  background:linear-gradient(180deg,#6e8a8f 0%,#4f6f78 35%,#2f5563 60%,#113543 88%,var(--deep) 100%)}
.hero-art::after{content:"";position:absolute;inset:0;
  background:radial-gradient(ellipse at 70% 40%,rgba(200,150,90,.25),transparent 45%),
             radial-gradient(ellipse at 10% 30%,rgba(30,90,80,.5),transparent 40%)}
.brand{left:74px;top:30px;width:160px;line-height:1}
.brand-name{font-size:42px;letter-spacing:1px;display:block}
.brand-sub{font-size:27px;display:block;text-align:right;padding-right:12px;margin-top:-2px}
.nav{top:60px;left:431px;font-size:16px}
.nav a{position:absolute;white-space:nowrap}
.hero-copy{left:74px;top:242px;font-size:35px;line-height:47px;letter-spacing:.6px;white-space:nowrap}
.btn{position:absolute;display:flex;align-items:center;justify-content:center;font-size:20px}
.btn-amber{background:var(--amber);color:var(--white)}
.btn-violet{background:var(--violet);color:var(--white);gap:8px}
.btn-line{border:2px solid var(--amber);color:var(--amber)}

.h-xl{font-size:62px;line-height:72px;letter-spacing:2px;white-space:nowrap}
.lead-lime{color:var(--lime);font-size:30px;line-height:41px;letter-spacing:.5px}
.body-copy{font-size:15.5px;line-height:28px}

.photo{position:absolute}
.photo-office{left:524px;top:787px;width:603px;height:433px;
  background:linear-gradient(160deg,#e7eef0 0%,#b9ccd2 35%,#5c8a6e 55%,#d9cbb3 80%,#c8b89c 100%)}
.photo-meeting{left:74px;top:1357px;width:601px;height:391px;
  background:linear-gradient(120deg,#2f5a2c 0%,#8fb36a 35%,#e6e4da 55%,#6c8b4e 80%,#27441f 100%)}

.services-band{left:0;top:1790px;width:1200px;height:655px;
  background:linear-gradient(180deg,var(--deep) 0%,#0b2d36 20%,#123a40 60%,#0a2a33 100%)}
.card-img{position:absolute;width:243px;height:183px}
.card-a{left:614px;top:1869px;background:linear-gradient(150deg,#f2f2f2,#c9cdd0 60%,#6d6f70)}
.card-b{left:885px;top:1869px;background:linear-gradient(150deg,#9aa0a4,#b83a3f 45%,#7a6a58 80%,#c5b49b)}
.card-title{position:absolute;top:2070px;color:var(--lime);font-size:22px;line-height:27px}
.card-arrow{position:absolute;top:2081px}

.badge{left:872px;top:2198px;width:223px;height:152px}

.footer{left:0;top:2445px;width:1200px;height:325px;background:var(--cream);color:var(--ink)}
.footer .brand{left:74px;top:128px}
.f-col{position:absolute;top:72px}
.f-col h4{font-weight:400;color:var(--violet);font-size:17px;margin-bottom:6px;letter-spacing:.3px}
.f-col li{list-style:none;font-size:13.5px;line-height:27px}
.contact-row{display:flex;gap:12px;font-size:13.5px;line-height:27px}
.contact-row svg{flex:none;margin-top:6px}
.chat{left:1126px;top:2741px;width:44px;height:44px;border-radius:50%;background:var(--amber);display:flex;align-items:center;justify-content:center}
.legal{left:0;top:2770px;width:1200px;height:78px;background:var(--violet);color:var(--white);font-size:13px;display:flex;align-items:center;justify-content:center}
</style>
</head>
<body>

<div class="abs hero-art" role="img" aria-label="Illustration of a designer working at a desk surrounded by large leafy plants"></div>

<header>
  <a class="abs brand" href="#"><span class="brand-name">Fernvale</span><span class="brand-sub">pte ltd</span></a>
  <nav class="abs nav">
    <a style="left:0">Home</a>
    <a style="left:92px">Services</a>
    <a style="left:200px">Gallery</a>
    <a style="left:299px">Calculator</a>
    <a style="left:421px">Testimonials</a>
    <a style="left:557px">Blog</a>
    <a style="left:636px">Contact</a>
  </nav>
</header>

<p class="abs hero-copy">Bring goods straight from factory<br>and cut away the middleman costing<br>so client can have a better quality<br>with affordable price.</p>
<a class="btn btn-amber" style="left:74px;top:454px;width:178px;height:54px">Read More</a>
<a class="btn btn-violet" style="left:263px;top:454px;width:179px;height:54px">
  <svg width="22" height="22" viewBox="0 0 22 22"><circle cx="11" cy="11" r="9.5" fill="none" stroke="#fff" stroke-width="2"/><path d="M8.5 6.5l7 4.5-7 4.5z" fill="#fff"/></svg>Play Video</a>

<h2 class="abs h-xl" style="left:74px;top:852px">Our Portfolio</h2>
<p class="abs lead-lime" style="left:74px;top:933px;width:420px">Explore our work.<br>Let our design portfolio<br>speaks for itself.</p>
<a class="btn btn-line" style="left:75px;top:1093px;width:179px;height:55px">View All Project</a>
<div class="photo photo-office" role="img" aria-label="Photo of a bright open-plan office with skylight, desks and potted trees"></div>

<div class="photo photo-meeting" role="img" aria-label="Photo of a team meeting at a table in a plant-filled office"></div>
<h2 class="abs h-xl" style="left:704px;top:1348px;line-height:68px">Welcome to<br>fernvale</h2>
<p class="abs" style="left:704px;top:1492px;width:440px;color:var(--lime);font-size:25px;line-height:33px">A Singapore Reputable Commercial<br>Interior Design &amp; Office Renovation<br>Company</p>
<p class="abs body-copy" style="left:704px;top:1596px;width:440px">No matter what type of commercial space you have,<br>whether it is an office, corporate firm, restaurant, spa, salon,<br>plaza, mall, or any retail shop.</p>
<a class="btn btn-line" style="left:704px;top:1694px;width:179px;height:54px">Read More</a>

<div class="abs services-band" role="img" aria-label="Dim photo of people working in a modern office"></div>
<h2 class="abs h-xl" style="left:76px;top:1856px">Our Services</h2>
<p class="abs body-copy" style="left:76px;top:1943px;width:500px">Sed ut perspiciatis unde omnis iste natus error sit voluptatem<br>accusantium doloremque laudantium  inventore veritatis et quasi<br>architecto beatae vitae dicta sunt explicabo.</p>
<a class="btn btn-line" style="left:75px;top:2057px;width:179px;height:55px">View All</a>

<div class="card-img card-a" role="img" aria-label="Photo of a white minimalist office interior"></div>
<p class="card-title" style="left:614px">Office Interior<br>Design</p>
<svg class="card-arrow" style="left:836px" width="22" height="22" viewBox="0 0 22 22"><circle cx="11" cy="11" r="9.5" fill="none" stroke="var(--amber)" stroke-width="2.4"/><path d="M6 11h9M11.5 7l4 4-4 4" fill="none" stroke="var(--amber)" stroke-width="2.4"/></svg>

<div class="card-img card-b" role="img" aria-label="Photo of a renovated office with red chairs and exposed ceiling"></div>
<p class="card-title" style="left:885px">Office<br>Renovation</p>
<svg class="card-arrow" style="left:1106px" width="22" height="22" viewBox="0 0 22 22"><circle cx="11" cy="11" r="9.5" fill="none" stroke="var(--amber)" stroke-width="2.4"/><path d="M6 11h9M11.5 7l4 4-4 4" fill="none" stroke="var(--amber)" stroke-width="2.4"/></svg>

<h3 class="abs" style="left:120px;top:2222px;font-size:36px;font-weight:400;letter-spacing:1px">Awards</h3>
<p class="abs body-copy" style="left:120px;top:2270px;white-space:nowrap">Each year Evergrow 500 is a way to recognise the top-performing Small-Medium Enterprises (SMEs).<br>It includes all business industries and sectors in Singapore.</p>
<svg class="abs badge" viewBox="0 0 223 152" role="img" aria-label="Award badge"><rect x="30" y="10" width="163" height="132" rx="10" fill="none" stroke="#fff" stroke-width="3"/></svg>

<footer class="abs footer">
  <a class="abs brand" href="#"><span class="brand-name">Fernvale</span><span class="brand-sub">pte ltd</span></a>
  <div class="f-col" style="left:279px"><h4>SITE MAP</h4><ul><li>Home</li><li>Services</li><li>Gallery</li><li>Calculator</li><li>Testimonials</li><li>Blog</li><li>Contact</li></ul></div>
  <div class="f-col" style="left:446px"><h4>SERVICES</h4><ul><li>Services Overview</li><li>Office Interior Design</li><li>Office Renovation</li><li>Office Space Planning</li><li>Office Partitioning</li></ul></div>
  <div class="f-col" style="left:655px"><h4>CALCULATOR TOOLS</h4><ul><li>Office Space Calculator</li><li>Renovation Budget Calculator</li><li>Project Timeline Calculator</li></ul></div>
  <div class="f-col" style="left:884px"><h4>CONTACT INFO</h4>
    <div class="contact-row"><svg width="17" height="14" viewBox="0 0 17 14"><path d="M0 2l5-2 6 2 6-2v12l-6 2-6-2-5 2z" fill="var(--violet)"/></svg><span>21 Leafbrook Road<br>#04-11 Canopy House,<br>Singapore 108812</span></div>
    <div class="contact-row" style="margin-top:6px"><svg width="17" height="14" viewBox="0 0 17 14"><path d="M3 1l3 3-2 2c1 2 2 3 4 4l2-2 3 3-2 2C6 13 1 8 1 3z" fill="var(--violet)"/></svg><span>+65 6100 2738</span></div>
    <div class="contact-row" style="margin-top:6px"><svg width="17" height="14" viewBox="0 0 17 14"><rect x="0" y="1" width="16" height="11" fill="var(--violet)"/><path d="M0 1l8 6 8-6" fill="none" stroke="var(--cream)" stroke-width="1.4"/></svg><span>hello@fernvale.example</span></div>
  </div>
</footer>

<a class="abs chat" aria-label="Chat"><svg width="22" height="18" viewBox="0 0 22 18"><path d="M2 1h11a1 1 0 011 1v7a1 1 0 01-1 1H7l-4 3v-3H2a1 1 0 01-1-1V2a1 1 0 011-1z" fill="#fff"/><path d="M16 5h4a1 1 0 011 1v7a1 1 0 01-1 1h-1v3l-4-3h-5a1 1 0 01-1-1v-1h5a2 2 0 002-2z" fill="#fff"/></svg></a>

<div class="abs legal">© 2023.All Company Name Right Reserved &nbsp; | Office Design and Renovation. All Rights Reserved.</div>

</body>
</html>
```